Financial Advisor Graphic to Explain Proprietary and Differentiating Investment Strategy

We need a graphic that visualizes how we build a portfolio based on factors of the underlying companies. We use 8 main factors to objectively build an investment porftolio. Our colors are blues, greys (see www.pltvexgroup.com). We are thinking either a venn diagram approach or an atom approach with the factors around the middle "Core Portfolio". This is what differentiates us from everyone in the industry. This will be the key to all of our marketing

Target Market(s)

High net worth investors

Industry/Entity Type

Financial Service

Font styles to use
Serif

Requirements
Must have
• Graphic must be elegant. It is for the financial industry. It should include the following factors (in no order) to build a "Core Portfolio"
• -Counter Cyclical Industries
• -Industry Rate of Recovery
• -Price To Book
• -Absolute Risk
• -Market Capitalization
• -Liquidity
• -Dividend Yield
• -Buy Back Yield
Nice to have
• We are thinking an atom approach or a venn diagram but we are open to new ideas. It must portray the idea that we OBJECTIVELY apply these factors to stock selection to build a core portfolio for our investors. For color pallets see www.pltvexgroup.com It can go beyond the greys and blues but should not be too loud or playful. It can be high tech as long as it portrays seriousness of the financial markets
Should not have
• Can not be playful.

```html
<!DOCTYPE html>
<html lang="en">
<head>
<meta charset="utf-8">
<title>Core Portfolio – Eight Factors</title>
<link rel="stylesheet" href="https://fonts.googleapis.com/css2?family=Oswald:wght@400&family=Montserrat:wght@700&display=swap">
<style>
  :root {
    --navy: #1b1a5c;
    --ink: #3b3b40;
    --ring: #9ea3ad;
    --ring-light: #c8cbd2;
    --paper: #ffffff;
    --mist: #eceef1;
  }
  html, body {
    margin: 0;
    padding: 0;
    width: 1200px;
    height: 1200px;
    overflow: hidden;
    background: var(--paper);
  }
  .factor-diagram {
    display: block;
    width: 1200px;
    height: 1200px;
  }
  .factor-label {
    font-family: "Oswald", "Arial Narrow", sans-serif;
    font-weight: 400;
    font-size: 23px;
    fill: var(--ink);
    text-anchor: middle;
  }
  .core-title {
    font-family: "Montserrat", "Helvetica", sans-serif;
    font-weight: 700;
    font-size: 35px;
    letter-spacing: 1px;
    fill: var(--navy);
    text-anchor: middle;
  }
</style>
</head>
<body>
<svg class="factor-diagram" viewBox="0 0 1100 1100" xmlns="http://www.w3.org/2000/svg" role="img" aria-label="Core Portfolio built from eight factors">
  <defs>
    <radialGradient id="backdrop" cx="50%" cy="50%" r="50%">
      <stop offset="0%" stop-color="#f3f4f6"/>
      <stop offset="70%" stop-color="#f7f8f9"/>
      <stop offset="100%" stop-color="#ffffff"/>
    </radialGradient>
    <linearGradient id="core-fill" x1="0" y1="0" x2="1" y2="1">
      <stop offset="0%" stop-color="#ffffff"/>
      <stop offset="60%" stop-color="#f1f2f4"/>
      <stop offset="100%" stop-color="#dcdee2"/>
    </linearGradient>
    <filter id="soft-shadow" x="-30%" y="-30%" width="160%" height="160%">
      <feDropShadow dx="4" dy="8" stdDeviation="9" flood-color="#1b1a5c" flood-opacity="0.22"/>
    </filter>
    <filter id="core-shadow" x="-30%" y="-30%" width="160%" height="160%">
      <feDropShadow dx="10" dy="14" stdDeviation="14" flood-color="#000" flood-opacity="0.18"/>
    </filter>
    <g id="factor-pin">
      <circle cx="0" cy="-370" r="100" fill="var(--navy)"/>
      <path d="M -70.7,-299.3 C -42,-272 -28,-250 -24,-222 L 24,-222 C 28,-250 42,-272 70.7,-299.3 Z" fill="var(--navy)"/>
      <circle cx="0" cy="-217" r="20" fill="var(--navy)"/>
      <circle cx="0" cy="-217" r="12" fill="var(--paper)"/>
      <circle cx="0" cy="-370" r="80" fill="var(--paper)"/>
    </g>
  </defs>

  <rect class="backdrop" width="1100" height="1100" fill="url(#backdrop)"/>

  <g class="orbit-rings" fill="none">
    <circle cx="550" cy="550" r="240" stroke="var(--ring-light)" stroke-width="2" stroke-dasharray="128.5 60" stroke-dashoffset="158.5"/>
    <circle cx="550" cy="550" r="217" stroke="var(--ring)" stroke-width="2.5"/>
    <circle cx="550" cy="550" r="195" stroke="var(--ring-light)" stroke-width="1.5" stroke-dasharray="103 50" stroke-dashoffset="128"/>
  </g>

  <g class="factor-pins" filter="url(#soft-shadow)">
    <use href="#factor-pin" transform="translate(550 550) rotate(0)"/>
    <use href="#factor-pin" transform="translate(550 550) rotate(45)"/>
    <use href="#factor-pin" transform="translate(550 550) rotate(90)"/>
    <use href="#factor-pin" transform="translate(550 550) rotate(135)"/>
    <use href="#factor-pin" transform="translate(550 550) rotate(180)"/>
    <use href="#factor-pin" transform="translate(550 550) rotate(225)"/>
    <use href="#factor-pin" transform="translate(550 550) rotate(270)"/>
    <use href="#factor-pin" transform="translate(550 550) rotate(315)"/>
  </g>

  <g class="core">
    <circle cx="550" cy="550" r="176" fill="url(#core-fill)" filter="url(#core-shadow)"/>
    <text class="core-title" x="550" y="527">CORE</text>
    <text class="core-title" x="550" y="571">PORTFOLIO</text>
  </g>

  <g class="factor-labels">
    <text class="factor-label" x="548" y="172"><tspan x="548">ABSOLUTE</tspan><tspan x="548" dy="28">RISK</tspan></text>
    <text class="factor-label" x="809" y="264"><tspan x="809">INDUSTRY</tspan><tspan x="809" dy="28">RATE OF</tspan><tspan x="809" dy="28">RECOVERY</tspan></text>
    <text class="factor-label" x="918" y="536"><tspan x="918">PRICE</tspan><tspan x="918" dy="28">TO BOOK</tspan></text>
    <text class="factor-label" x="810" y="804"><tspan x="810">DIVIDEND</tspan><tspan x="810" dy="28">YIELD</tspan></text>
    <text class="factor-label" x="550" y="912"><tspan x="550">MARKET</tspan><tspan x="550" dy="28">CAPITALIZATION</tspan></text>
    <text class="factor-label" x="287" y="804"><tspan x="287">BUY BACK</tspan><tspan x="287" dy="28">YIELD</tspan></text>
    <text class="factor-label" x="176" y="557">LIQUIDITY</text>
    <text class="factor-label" x="285" y="260"><tspan x="285">COUNTER</tspan><tspan x="285" dy="28">CYCLICAL</tspan><tspan x="285" dy="28">INDUSTRIES</tspan></text>
  </g>
</svg>
</body>
</html>
```